Wageline Associates Business Card Design

We need a business card designed around our new logo. The business card should be modern in design & should communicate success, confidence, power, sophistication. The target market is young business professionals. This is for a human resource & payroll outsourcing business.

```html
<!DOCTYPE html>
<html lang="en">
<head>
<meta charset="utf-8">
<title>Wageline Associates Business Card</title>
<link rel="stylesheet" href="https://fonts.googleapis.com/css2?family=Roboto:wght@400;500;700&display=swap">
<style>
  :root {
    --bg: #6f7b80;
    --card: #ffffff;
    --ink: #111111;
    --accent: #e3161b;
  }
  * { margin: 0; padding: 0; box-sizing: border-box; }
  html, body { width: 1200px; height: 900px; overflow: hidden; }
  body {
    background: var(--bg);
    font-family: "Roboto", Arial, sans-serif;
    color: var(--ink);
    display: flex;
    flex-direction: column;
    align-items: center;
    justify-content: center;
    gap: 40px;
  }
  .card {
    position: relative;
    width: 620px;
    height: 354px;
    background: var(--card);
    border-radius: 22px;
    box-shadow: 0 10px 24px rgba(0,0,0,0.25);
  }
  .brand {
    display: flex;
    align-items: center;
    gap: 10px;
  }
  .brand-dot {
    width: 16px; height: 16px;
    border-radius: 50%;
    background: var(--accent);
    flex: none;
  }
  .brand-name {
    font-weight: 500;
    color: var(--ink);
    letter-spacing: 0.5px;
    white-space: nowrap;
  }
  /* front */
  .card-front .brand {
    position: absolute;
    top: 140px; left: 0; right: 0;
    justify-content: center;
  }
  .card-front .brand-name { font-size: 40px; }
  .card-front .brand-dot { width: 22px; height: 22px; }
  .web-front {
    position: absolute;
    bottom: 34px; left: 0; right: 0;
    text-align: center;
    font-size: 14px;
  }
  /* back */
  .card-back .brand {
    position: absolute;
    top: 56px; left: 48px;
  }
  .card-back .brand-name { font-size: 28px; }
  .holder {
    position: absolute;
    top: 48px; right: 40px;
    text-align: right;
  }
  .holder-name {
    font-size: 21px;
    font-weight: 700;
    letter-spacing: 0.3px;
  }
  .holder-name .surname { color: var(--accent); font-weight: 500; }
  .holder-role { font-size: 12px; margin-top: 2px; }
  .rule {
    position: absolute;
    top: 176px; left: 120px; right: 40px;
    height: 2px;
    background: var(--accent);
  }
  .address {
    position: absolute;
    top: 218px; right: 40px;
    text-align: right;
    font-size: 15px;
    line-height: 1.4;
  }
  .contacts {
    position: absolute;
    top: 196px; left: 120px;
    list-style: none;
  }
  .contacts li {
    display: flex;
    align-items: center;
    gap: 14px;
    height: 31px;
    font-size: 16px;
  }
  .icon {
    width: 22px; height: 22px;
    background: var(--ink);
    display: flex; align-items: center; justify-content: center;
    flex: none;
  }
  .icon svg { width: 16px; height: 16px; }
</style>
</head>
<body>

  <section class="card card-front" aria-label="Card front">
    <div class="brand">
      <span class="brand-dot"></span>
      <span class="brand-name">Wageline Associates</span>
    </div>
    <p class="web-front">www.wagelinehq.com</p>
  </section>

  <section class="card card-back" aria-label="Card back">
    <div class="brand">
      <span class="brand-dot"></span>
      <span class="brand-name">Wageline Associates</span>
    </div>

    <div class="holder">
      <p class="holder-name">DANIEL <span class="surname">REYES</span></p>
      <p class="holder-role">Founder &amp; Director</p>
    </div>

    <div class="rule"></div>

    <ul class="contacts">
      <li>
        <span class="icon"><svg viewBox="0 0 16 16"><path fill="#fff" d="M3 2l3 0 1 3-2 1c1 2 2 3 4 4l1-2 3 1 0 3c-6 0-10-4-10-10z"/></svg></span>
        415-555-0182
      </li>
      <li>
        <span class="icon"><svg viewBox="0 0 16 16"><rect x="2" y="6" width="12" height="8" rx="1" fill="none" stroke="#fff" stroke-width="1.4"/><path d="M4 6V3h6l2 2v1" fill="none" stroke="#fff" stroke-width="1.4"/><rect x="5" y="9" width="6" height="2" fill="#fff"/></svg></span>
        415-555-0147
      </li>
      <li>
        <span class="icon"><svg viewBox="0 0 16 16"><rect x="2" y="4" width="12" height="8" fill="none" stroke="#fff" stroke-width="1.4"/><path d="M2 4l6 5 6-5" fill="none" stroke="#fff" stroke-width="1.4"/></svg></span>
        hello@wagelinehq.com
      </li>
      <li>
        <span class="icon"><svg viewBox="0 0 16 16"><circle cx="8" cy="8" r="6" fill="none" stroke="#fff" stroke-width="1.4"/><ellipse cx="8" cy="8" rx="2.5" ry="6" fill="none" stroke="#fff" stroke-width="1.2"/><path d="M2 8h12" stroke="#fff" stroke-width="1.2"/></svg></span>
        www.wagelinehq.com
      </li>
    </ul>

    <p class="address">48 Harbor Street - Northfield<br>Lakeview 20417</p>
  </section>

</body>
</html>
```